Marketing Brochure For Tallbrook LLC for marketing and advertising purposes.A slick and modern design. I have added in the attachment a PDF called Tallbrook Profile which is the old version of this new one we are creating but can give you an idea of what I am looking for. I also have a Word document called New Consulting Document that lists each topic, where the attached images go, and the wording that goes in each. The total brochure should be between 8 and 12 pages.

Industry/Entity Type

Credit Card

Font styles to use
Serif

Colors
f78f20
886aae

Requirements
Must have
• A slick and modern design. I have added in the attachment a PDF called Tallbrook Profile which is the old version of this new one we are creating but can give you an idea of what I am looking for. I also have a Word document called New Consulting Document that lists each topic, where the attached images go, and the wording that goes in each. The total brochure should be between 8 and 12 pages.

```html
<!DOCTYPE html>
<html lang="en">
<head>
<meta charset="utf-8">
<title>Tallbrook LLC — Services Brochure</title>
<link href="https://fonts.googleapis.com/css2?family=Fira+Sans+Condensed:ital,wght@0,400;0,500;0,600;1,700&family=Roboto+Condensed:wght@400;700&display=swap" rel="stylesheet">
<style>
:root{
  --orange:#f78f20;
  --purple:#886aae;
  --pink:#ee4c6a;
  --stage:#3a3a3c;
  --ink:#4a4a4a;
  --paper:#ffffff;
}
*{margin:0;padding:0;box-sizing:border-box}
html,body{width:1200px;height:1200px;overflow:hidden;background:var(--stage)}
body{position:relative;font-family:"Roboto Condensed",sans-serif;color:var(--ink)}
.page{position:absolute;width:382px;height:540px;background:var(--paper);overflow:hidden}
.page--tl{left:218px;top:34px;background:linear-gradient(90deg,#fff 88%,#efefef)}
.page--tr{left:600px;top:34px}
.page--bl{left:218px;top:625px;background:linear-gradient(90deg,#fff 88%,#efefef)}
.page--br{left:600px;top:625px}
.abs{position:absolute}
.section-title{position:absolute;font-family:"Fira Sans Condensed",sans-serif;font-weight:500;color:var(--purple);font-size:11px;padding-left:30px;white-space:nowrap}
.section-title::before{content:"";position:absolute;left:0;top:7px;width:20px;height:1.5px;background:var(--orange)}
.section-title::after{content:"";position:absolute;left:17px;top:2px;width:7px;height:7px;border:2px solid var(--orange);border-radius:50%;background:#fff}
.page--tr .section-title::before{left:-32px;width:52px}
.points{position:absolute;list-style:none;font-size:5.6px;line-height:8.6px;text-align:justify}
.points li{position:relative;margin-bottom:4px}
.points li::before{content:"";position:absolute;left:-9px;top:2.4px;width:4px;height:4px;border:1.2px solid #555;border-radius:50%}
.art{position:absolute;border:1.5px solid var(--orange);padding:3px;background:#fff}
.art span{display:block;width:100%;height:100%}
.hero-photo{left:0;top:0;width:382px;height:150px;background:linear-gradient(120deg,#dfe3e6,#f4f5f6 45%,#c9d0d6)}
.banner-title{position:absolute;left:0;width:382px;top:160px;text-align:center;font-family:"Fira Sans Condensed",sans-serif;font-style:italic;font-weight:700;color:#fff;font-size:19px;letter-spacing:-.2px}
.portrait{position:absolute;left:38px;top:29px;width:142px;height:142px;border-radius:50%;border:4px solid var(--orange);background:radial-gradient(circle at 50% 40%,#d9cfc8,#8a8f98 60%,#2d3340)}
.name{position:absolute;left:201px;top:71px;font-family:"Fira Sans Condensed",sans-serif;font-style:italic;font-weight:700;color:#fff;font-size:19px}
.role{position:absolute;left:213px;top:93px;font-family:"Fira Sans Condensed",sans-serif;font-style:italic;font-weight:600;color:#fff;font-size:7px}
.bio{position:absolute;left:47px;top:182px;width:287px;font-size:7.4px;line-height:10.6px;text-align:justify}
.badge{position:absolute;background:#2b5aa0}
.honors{position:absolute;list-style:none;font-size:5.3px;line-height:8.4px;color:var(--orange)}
.honors li::before{content:"• "}
.mark-name{position:absolute;font-family:"Roboto Condensed",sans-serif;font-weight:700;color:#222;font-size:9px}
.blog{position:absolute;left:0;top:339px;width:382px;height:143px;background:var(--purple);color:#e9e2f2}
.blog h2{position:absolute;left:34px;top:14px;font-family:"Fira Sans Condensed",sans-serif;font-style:italic;font-weight:700;color:#fff;font-size:19px}
.blog p{position:absolute;font-size:6.6px;line-height:9.2px;text-align:justify}
.events{position:absolute;left:0;top:482px;width:382px;height:58px;background:#fff}
.events .label{position:absolute;left:94px;top:18px;font-family:"Fira Sans Condensed",sans-serif;font-style:italic;font-weight:700;color:var(--orange);font-size:15px}
.events .ev{position:absolute;font-size:5.5px;color:#555}
.events .ev b{display:block;font-family:"Fira Sans Condensed",sans-serif;font-style:italic;font-size:7px;color:#222;margin-top:3px}
</style>
</head>
<body>

<section class="page page--tl">
  <div class="abs hero-photo" role="img" aria-label="Photo of two people at a desk reviewing and signing documents"></div>
  <svg class="abs" style="left:0;top:125px" width="382" height="75" viewBox="0 0 382 75">
    <defs><linearGradient id="band1" x1="0" x2="1"><stop offset="0" stop-color="#f78f20"/><stop offset="1" stop-color="#ee4c6a"/></linearGradient></defs>
    <polygon points="0,20 382,0 382,62 0,75" fill="url(#band1)"/>
  </svg>
  <div class="banner-title">›SERVICES PROVIDED</div>

  <h3 class="section-title" style="left:0;top:210px">Operational Excellence</h3>
  <ul class="points" style="left:41px;top:227px;width:178px">
    <li>We will provide an exhaustive and unbiased review of your organizations current collection strategies from a cradle to grave work flow standpoint. This will include best practices from across the industry and provide you with templated procedures, necessary reporting, workforce management, and ensuring your organization is working with the right technology providers at the right cost to the organization.</li>
    <li>We will also provide you with in-depth expert advice encompassing two decades of experience providing actionable solutions that will provide organizations with methods to increase recoveries, liquidation, and revenue.</li>
  </ul>
  <div class="art" style="left:225px;top:228px;width:125px;height:90px"><span role="img" aria-label="Sketch of strategy development icons and charts" style="background:linear-gradient(135deg,#f3f3f3,#dcdcdc)"></span></div>
  <ul class="points" style="left:41px;top:334px;width:308px">
    <li>If warranted, a full and complete review of the organizations profit, and loss statement would be reviewed and findings shared with executive management to identify areas and trends where the strengths and areas of opportunities are.</li>
  </ul>

  <h3 class="section-title" style="left:0;top:372px">Compliance</h3>
  <ul class="points" style="left:41px;top:387px;width:178px">
    <li>Perform an exhaustive review and determine the maturity of your organizations existing Compliance Management System</li>
    <li>Produce a framework to build upon a CMS from the current maturity level which includes development and/or enhancement of policies, procedures, controls, work instructions, exception reporting, and technology usage/opportunities.</li>
    <li>Having gone through several Guild Agency Standards Certification Program (ASCP) reviews as an agency owner and certified instructor we are prepared to assist your organization to fast track this critical component of an agency's compliance management system. We can save you time, money, and resources by assisting with the awesome program.</li>
  </ul>
  <div class="art" style="left:224px;top:386px;width:126px;height:91px"><span role="img" aria-label="Compliance concept sketch with rules, law and governance icons" style="background:linear-gradient(135deg,#fafafa,#e4e4e4)"></span></div>
  <ul class="points" style="left:41px;top:498px;width:308px">
    <li>If you are interested in learning how to implement processes that will streamline the state licensing and bonding, we can save you time, effort, and energy by showing you how to do it yourself or how to negotiate with the vendors available to assist you.</li>
  </ul>
</section>

<section class="page page--tr">
  <h3 class="section-title" style="left:32px;top:45px">Employee Development</h3>
  <ul class="points" style="left:41px;top:66px;width:178px">
    <li>When it comes to any organization, the number one asset is the employees. If you take care of your employees, they will take care of your consumers, and that will take care of your organization. Ultimately, all we do starts and ends with our employees and we have developed a training curriculum from the first day all the way through years of gainful employment.</li>
    <li>Unfortunately, the debt collection industry operates under several strict liability statutes which means all employees must always be perfect. We all realize that is an unreasonable request but a request that must be adhered to nonetheless. We spend a lot of time with employees on how to operate under these statutes and what they can do to mitigate violating the various laws they must follow but still performing at optimal levels.</li>
  </ul>
  <div class="art" style="left:226px;top:67px;width:124px;height:90px"><span role="img" aria-label="Hand drawing a people development diagram: train, educate, empower, reward" style="background:linear-gradient(135deg,#f2f2f2,#d8d8d8)"></span></div>
  <ul class="points" style="left:41px;top:182px;width:308px">
    <li>We will help build a foundation and create or enhance your current employee development program which includes orientation, initial and ongoing training, employee handbooks, training manuals, and talent evaluations and reviews for each department.</li>
  </ul>

  <h3 class="section-title" style="left:32px;top:243px">Operational Excellence</h3>
  <ul class="points" style="left:41px;top:263px;width:178px">
    <li>The bottom line is image is everything. If an organization wants to get their foot in the door with a prospective client then they must portray themselves in a light that exudes confidence, competence, and the ability to impress the potential prospect. We will work with your current branding and leverage our great marketing team to ensure everything from your initial brochure to your website is top notch to ensure that you will not just get one foot in the door, but both.</li>
    <li>If you do not have top notch corporate branding then regardless of how great your organization is or how great you think it is, getting an opportunity to realize your organizations full potential will be very difficult.</li>
  </ul>
  <div class="art" style="left:227px;top:264px;width:123px;height:90px"><span role="img" aria-label="Compliance concept sketch with rules and regulation icons" style="background:linear-gradient(135deg,#f4f4f4,#dedede)"></span></div>
  <ul class="points" style="left:41px;top:370px;width:308px">
    <li>We will build your corporate branding from A to Z that encompasses everything great about your organization while at the same time customizing it to meet the needs of your target market.</li>
    <li>Public relations also place a role in corporate branding and we will help you identify who or whom in your organization would be best suited to take the reigns of your public relations campaign.</li>
    <li>We will work with them and prepare them for everything they need to know to be successful while leveraging our vast network to position your organization into various opportunities that will pay dividends with existing clients and future partners.</li>
    <li>In addition to your employees, the second most asset to your organization is your clients or what I refer to as partners with the client experience. So why is there not enough emphasis placed on ensuring your partners experience is one they will never forget. There are so many little ways you can make your partners experience superlative and we can walk you through each of those ways in order to make sure your partners or just that, partners and not just another client.</li>
  </ul>
</section>

<section class="page page--bl">
  <h3 class="section-title" style="left:0;top:40px">Information Technology/Data Security</h3>
  <ul class="points" style="left:41px;top:61px;width:178px">
    <li>We will ensure that you are aware of all the options available to reduce costs, increase compliance, improve efficiency, and maximize overall performance. We understand that IT costs can be extremely costly, so it is important for us to lay out what options are out there and what they cost are while determining what other options may be best suited for your organization and still achieve the intended result.</li>
    <li>We have relationships with all the major and minor players in the collection software, telephony, skip-tracing, scoring, speech analytics, and other industry solutions in which we can leverage that network to obtain the best product at the lowest cost possible.</li>
  </ul>
  <div class="art" style="left:225px;top:60px;width:125px;height:91px"><span role="img" aria-label="Illustration of a technology network circle with devices around a chart" style="background:radial-gradient(circle,#e7eef3,#f7f7f7 70%)"></span></div>

  <h3 class="section-title" style="left:0;top:181px">Vendor Oversight</h3>
  <ul class="points" style="left:41px;top:202px;width:178px">
    <li>Whether you are a creditor or asset buyer who needs to oversee your outside vendor partners, Tallbrook is where you want to come to make that happen. Having spent two decades going through hundreds of audits in all scope and sizes, Tallbrook knows what creditors and asset buyers are looking for and in addition to the compliance end of the spectrum, we provide the added benefit of looking at the audit the operation lenses as well to see where opportunity may provide itself to increase revenue while mitigating risk.</li>
  </ul>
  <div class="art" style="left:225px;top:202px;width:125px;height:90px"><span role="img" aria-label="Audit concept illustration with a businessman, word cloud and red banner" style="background:linear-gradient(135deg,#f1f3f7,#dfe4ec)"></span></div>
  <ul class="points" style="left:41px;top:298px;width:308px">
    <li>As a collection agency, it is imperative that you are monitoring and auditing your vendors such as skip-tracing, telephony, collection software, and others. Tallbrook can either handle this for you or we can teach you and your team how to ensure you are auditing your vendors and following all applicable work standards and laws in this complicated area.</li>
  </ul>

  <h3 class="section-title" style="left:0;top:356px">Solution Providers</h3>
  <ul class="points" style="left:44px;top:376px;width:175px">
    <li>For vendors or as I refer to them as solution providers seeking to do business with creditors, asset buyers, and collection agencies then Tallbrook is the team you need to make it happen while we leverage our vast network to increase exposure and opportunity.</li>
    <li>Utilizing two decades of experience in the credit and collection industry while utilizing or testing most products on the market, we can provide an unparalleled and unique perspective regarding your product and service while providing candid feedback and what steps need to be taken in regards of areas of opportunities and outlining the strengths that need to be taken advantage of as well.</li>
  </ul>
  <div class="art" style="left:224px;top:374px;width:126px;height:91px"><span role="img" aria-label="Sketch of an accuracy concept with charts and office objects" style="background:linear-gradient(135deg,#f6f6f6,#e2e2e2)"></span></div>
  <ul class="points" style="left:44px;top:476px;width:305px">
    <li>In this program we will perform an exhaustive and unbiased review of your organizations product of service while providing cost and market analysis of similar products and services.</li>
  </ul>
</section>

<section class="page page--br">
  <svg class="abs" style="left:0;top:35px" width="382" height="120" viewBox="0 0 382 120">
    <defs><linearGradient id="band2" x1="0" x2="1"><stop offset="0" stop-color="#f78f20"/><stop offset="1" stop-color="#ee4c6a"/></linearGradient></defs>
    <polygon points="0,35 382,0 382,73 0,117" fill="url(#band2)"/>
  </svg>
  <div class="portrait" role="img" aria-label="Portrait photo of the company owner in a dark suit"></div>
  <div class="name">Owen Calder</div>
  <div class="role">Owner, Tallbrook, LLC.</div>
  <p class="bio">Owen Calder has two decades of experience encompassing all facets of credit and collection operations. As one of the most respected leaders in the credit and collection industry, Owen is a nationally recognized speaker, writer, and consultant. Owen served a three-year term on Cedar Credit Guild's Board of Directors and was the youngest elected President of the Prairie Collectors Association. He is adamant about leading by example and ensuring that in everything he does, it is done the "Tallbrook Way."</p>

  <div class="badge" style="left:60px;top:255px;width:26px;height:26px"></div>
  <div class="mark-name" style="left:43px;top:286px;font-size:7px;font-weight:400">Cedar Credit Guild</div>
  <ul class="honors" style="left:106px;top:255px">
    <li>Fellowship of Certified Recovery<br>&nbsp;&nbsp;Leaders</li>
    <li>Chapter Leader of the Year</li>
    <li>Certified Instructor</li>
    <li>Credit &amp; Collection Compliance officer</li>
    <li>Fellow and Scholar</li>
    <li>Board of Directors (2013-2016)</li>
  </ul>
  <div class="badge" style="left:238px;top:257px;width:9px;height:9px;border-radius:50%;background:#222"></div>
  <div class="mark-name" style="left:250px;top:255px">Ledger Review</div>
  <ul class="honors" style="left:236px;top:273px">
    <li>Top 25 Voices in Receivables<br>&nbsp;&nbsp;Management</li>
    <li>Leaders in Receivables</li>
    <li>Top Rule Experts</li>
  </ul>

  <div class="blog">
    <h2>›BLOG</h2>
    <p style="left:26px;top:48px;width:155px">Tallbrook's Weekly Blog contains actionable solutions with a run down of the top industry stories from the prior week.<br><br>Tallbrook also puts on industry leading events that challenge the norm and set the standard for how industry events should be run. All</p>
    <p style="left:202px;top:10px;width:155px">of Tallbrook events are created to provide quality content at a reasonable price-point while providing real world solutions to real world problems. Our events provide a foundation of direction, insight, and actionable solutions that can be applied regardless of the size of an organization. Expert speakers with customized solutions for each event set our forums apart from other industry events.</p>
  </div>

  <div class="events">
    <div class="label">EVENT</div>
    <svg class="abs" style="left:141px;top:13px" width="14" height="30" viewBox="0 0 14 30"><polyline points="2,2 12,15 2,28" fill="none" stroke="#f78f20" stroke-width="3"/></svg>
    <div class="ev" style="left:176px;top:14px"><span style="color:#2b5aa0">Rule Summit</span><b>Fall Event</b></div>
    <div class="abs" style="left:226px;top:10px;width:1px;height:38px;background:#ccc"></div>
    <div class="ev" style="left:250px;top:14px"><span style="color:#c03040">Recovery Forum</span><b>Spring Event</b></div>
  </div>
</section>

</body>
</html>
```